Business Card Design for Tidewell

The company provides engineering tender consulting services and personnel resources. The target market is large engineering construction and services companies. The business is based in Australia.

```html
<!DOCTYPE html>
<html lang="en">
<head>
<meta charset="utf-8">
<title>Tidewell — Business Card</title>
<link rel="stylesheet" href="https://fonts.googleapis.com/css2?family=Source+Sans+3:wght@400;600;700&display=swap">
<style>
  :root {
    --stage: #2b2b2b;
    --blue: #1a9ad6;
    --blue-light: #5cc3ec;
    --blue-pale: #9fdcf5;
    --ink: #1e1e1e;
    --ink-soft: #555555;
    --card-light-top: #f4f4f4;
    --card-light-bottom: #cfcfcf;
    --card-dark: #0d0d0d;
    --ghost-light: rgba(0, 0, 0, 0.07);
    --ghost-dark: rgba(255, 255, 255, 0.12);
    --paper: #ffffff;
  }
  * { margin: 0; padding: 0; box-sizing: border-box; }
  html, body { width: 1200px; height: 820px; overflow: hidden; }
  body {
    background: var(--stage);
    font-family: "Source Sans 3", "Helvetica Neue", Arial, sans-serif;
    display: flex;
    align-items: center;
    justify-content: center;
    gap: 60px;
  }
  .card {
    position: relative;
    width: 520px;
    height: 300px;
    overflow: hidden;
    box-shadow: 0 6px 18px rgba(0,0,0,0.45);
  }

  /* ---------- Front ---------- */
  .card--front {
    background: linear-gradient(180deg, var(--card-light-top) 0%, #e6e6e6 55%, var(--card-light-bottom) 100%);
    color: var(--ink);
  }
  .top-band {
    position: absolute; left: 0; right: 0; top: 0; height: 16px;
    background: linear-gradient(90deg, var(--blue-pale) 0%, var(--blue-light) 35%, var(--blue) 70%, #4db8e6 100%);
  }
  .graphic-area {
    position: absolute; left: 0; bottom: 12px; z-index: 0;
  }
  .card--front .graphic-area {
    width: 250px; height: 110px;
    background: linear-gradient(90deg, #bdbdbd 0%, #d0d0d0 60%, rgba(220,220,220,0) 100%);
  }
  .holder {
    position: absolute; right: 18px; top: 22px; text-align: right; z-index: 2;
  }
  .holder__name { font-size: 19px; font-weight: 400; color: var(--ink); line-height: 1; }
  .holder__role { font-size: 10px; color: var(--ink-soft); margin-top: 3px; }
  .ghost-word {
    position: absolute; font-weight: 700; white-space: nowrap; line-height: 1;
    pointer-events: none; z-index: 1;
  }
  .card--front .ghost-word { left: 120px; top: 52px; font-size: 86px; color: var(--ghost-light); }
  .brand-strip {
    position: absolute; left: 0; top: 118px; width: 300px; height: 56px; z-index: 2;
    background: var(--paper);
    box-shadow: 0 2px 6px rgba(0,0,0,0.15);
  }
  .brand-name {
    position: absolute; left: 30px; top: 120px; z-index: 3;
    font-size: 46px; font-weight: 700; color: var(--blue); line-height: 1.1;
  }
  .contact {
    position: absolute; right: 18px; top: 150px; text-align: right; z-index: 2;
    font-size: 11px; color: var(--ink-soft); line-height: 1.55;
  }
  .contact__company { font-size: 19px; font-weight: 700; color: var(--ink); line-height: 1.2; }
  .bottom-band {
    position: absolute; left: 0; right: 0; bottom: 0; height: 12px;
    background: linear-gradient(90deg, #bdbdbd, #e0e0e0);
  }

  /* ---------- Back ---------- */
  .card--back { background: var(--card-dark); color: var(--paper); }
  .card--back .top-band { height: 10px; }
  .card--back .graphic-area {
    width: 200px; height: 170px;
    background: linear-gradient(90deg, #3a3a3a 0%, #262626 55%, rgba(13,13,13,0) 100%);
  }
  .about {
    position: absolute; left: 150px; right: 16px; top: 20px; z-index: 2;
    font-size: 9.5px; line-height: 1.4; color: #e8e8e8;
  }
  .card--back .ghost-word { left: 30px; top: 92px; font-size: 72px; color: var(--ghost-dark); }
  .services { position: absolute; left: 0; top: 0; width: 100%; height: 100%; z-index: 2; }
  .service { position: absolute; white-space: nowrap; color: #f2f2f2; line-height: 1; }
  .card--back .bottom-band { height: 12px; background: linear-gradient(90deg, #9a9a9a, #e5e5e5); }
</style>
</head>
<body>

  <section class="card card--front" aria-label="Business card front">
    <div class="top-band"></div>
    <div class="graphic-area" role="img" aria-label="Layered grey arrow graphic"></div>
    <div class="ghost-word">Tidewell</div>
    <div class="holder">
      <div class="holder__name">Firstname Surname</div>
      <div class="holder__role">Designation</div>
    </div>
    <div class="brand-strip"></div>
    <div class="brand-name">Tidewell</div>
    <div class="contact">
      <div class="contact__company">Tidewell</div>
      <div>PO Box 99 Nnnnnnnnnn, Nnn, 9999</div>
      <div>ABN99999999999</div>
      <div>M: 9999 999 999</div>
      <div>T: 99 9999 9999</div>
      <div>E: nnnn@nnn.com.au</div>
    </div>
    <div class="bottom-band"></div>
  </section>

  <section class="card card--back" aria-label="Business card back">
    <div class="top-band"></div>
    <div class="graphic-area" role="img" aria-label="Layered dark arrow graphic"></div>
    <p class="about">Tidewell provides engineering tender consulting and personnel resources. With a experience of bid management, business process outsourcing, hands-on, integrated implementation. Unlike others, we bring practical problem solving experience with tenders that help businesses and organizations grow and expand as markets change.</p>
    <div class="ghost-word">Tidewell</div>
    <div class="services">
      <span class="service" style="left:130px;top:172px;font-size:10px;">Project Management</span>
      <span class="service" style="left:250px;top:170px;font-size:13px;">Logical &amp; Creative Thinking</span>
      <span class="service" style="left:140px;top:186px;font-size:14px;">Strategic Planning</span>
      <span class="service" style="left:260px;top:190px;font-size:10px;">Value Management</span>
      <span class="service" style="left:175px;top:204px;font-size:16px;">Bid Management and Strategy</span>
      <span class="service" style="left:145px;top:223px;font-size:10px;">Independent estimations</span>
      <span class="service" style="left:278px;top:222px;font-size:10px;">Risk Management</span>
      <span class="service" style="left:208px;top:235px;font-size:10px;">Independent estimations</span>
      <span class="service" style="left:165px;top:250px;font-size:9px;">Total asset Management</span>
      <span class="service" style="left:300px;top:248px;font-size:12px;">Cost Management</span>
    </div>
    <div class="bottom-band"></div>
  </section>

</body>
</html>
```